Brightford Lingua Partners, LLC

We need a business card that includes information about our business and conveys a reliable business that provides document translation services and interpreters for a variety of corporate and individual clients. We want to come across as professional, reliable, yet approachable. It should include the following on one side:

ESL / ENL Language Classes, Private Lessons, and Online Tutors
PALQE Training and Testing
Translating & Interpreting Services
Contact us about Over-the-Phone Interpreting in over 200 languages
24/7/365
www.brightfordlingua.example

The other side should include (555) 481-3062

Marla Quennick, President
412 Garvin Ave., Ste. 209
Indianapolis, IN 46999
Updates

Please add USA as part of the address. Also, please add mrqquennick@brightfordlinguapartners.example as the e-mail address. Thank you.

Target Market(s)

Business professionals, their families, the international community

Industry/Entity Type

Business

Contact Information for Business Card

24/7/365
www.brightfordlingua.example

(555) 481-3062

Marla Quennick, President
412 Garvin Ave., Ste. 209
Indianapolis, IN 46999
USA

Font styles to use
Sans Serif

Colors

Designer to choose colors to be used in the design.

Requirements
Must have
• See project description
• e-mail address and web address
• Phone number
Nice to have
• a globe
• physical address
Should not have
• Should not have the same color scheme as other agencies in our market in Indiana unless it is blue and black. No purple or yellow.

```html
<!DOCTYPE html>
<html lang="en">
<head>
<meta charset="utf-8">
<title>Brightford Lingua Partners – Business Card Back</title>
<link rel="stylesheet" href="https://fonts.googleapis.com/css2?family=Jost:wght@700&family=Open+Sans:wght@400&display=swap">
<style>
  :root {
    --page-bg: #ffffff;
    --card-bg: #ffffff;
    --card-border: #8a8a8a;
    --ink: #000000;
  }
  html, body {
    margin: 0;
    padding: 0;
    width: 1200px;
    height: 1200px;
    overflow: hidden;
    background: var(--page-bg);
  }
  .canvas {
    position: relative;
    width: 1200px;
    height: 1200px;
  }
  .card {
    position: absolute;
    left: 120px;
    top: 389px;
    width: 970px;
    height: 462px;
    box-sizing: border-box;
    border: 1px solid var(--card-border);
    background: var(--card-bg);
    color: var(--ink);
    text-align: center;
  }
  .card__phone {
    position: absolute;
    left: 0;
    right: 0;
    top: 100px;
    margin: 0;
    font-family: "Jost", "Futura", sans-serif;
    font-weight: 700;
    font-size: 35px;
    line-height: 1;
    word-spacing: 6px;
    letter-spacing: -0.5px;
  }
  .card__contact {
    position: absolute;
    left: 0;
    right: 0;
    top: 170px;
    margin: 0;
    font-family: "Open Sans", "Segoe UI", sans-serif;
    font-style: normal;
    font-weight: 400;
    font-size: 27px;
    line-height: 40px;
  }
  .card__email {
    display: block;
  }
</style>
</head>
<body>
  <div class="canvas">
    <section class="card" aria-label="Business card, contact side">
      <p class="card__phone">(555) 481-3062</p>
      <address class="card__contact">
        Marla Quennick, President<br>
        412 Garvin Ave., Ste. 209<br>
        Indianapolis, IN 46999<br>
        USA
        <span class="card__email">mrqquennick@brightfordlinguapartners.example</span>
      </address>
    </section>
  </div>
</body>
</html>
```